Systems and Technology Consultants - Website

Design & Build a website for a new company which operates in the Systems and Technology space for Transportation, Government and Commercial sectors.

Overall design should be minimalist in nature.
Should also have a feed that provides news and event updates on the main page.
Logo has already been awarded and should be incorporated into the site.

We like the overall layout, functionality and simplicity of the below sites. Submitted designs could be similar to or a combination of the aspects on these sites, or perhaps a whole different concept - we are open to new ideas.
Vortrane.com
Merp.it

Update 1 Dated 27 May 2014

All I am moving away from the Merp.it website and would like it to be more aligned with Vortrane.com not only in layout but in functionality. I will be extending the deadline of this design brief for two weeks to incorporate additional requirements and will add addtional funding to the project.

Apologies for not having more information available to provide but with so many submissions its getting confusing.

Thanks Dermot
Updates

Please note that the brief has been updated and the deadline has been extended.

Important: We will need two language versions of the website, English and Arabic; the website is hosted on HostPeak

Hello All, Thank you for your submissions. We have narrowed it down to the final 6 designers and I just wanted to take a moment and provide a bit of feedback regarding the concepts that we like and the modifications we are looking for. First, let me mention some of the design functions we like. - At the top of the homepage we really like the "region" or "language" tab so that the website can be viewed in both English and Arabic. - We like the homepage to have clear color variation so that the different sections of the homepage are distinct. Additionally, we like the bottom portion of the homepage to be in red. We feel that draws attention to our contact information. Again, we would like the colors to integrate black, gray-scale, red, etc. - Having a search tab at the top of the home page, or integrated into the main image, so that the site is easy to navigate. - We especially like the main image to have the scrolling tabs at the bottom so it is easy to browse the services offered (Consultancy, Solutions Architecture, Masters Systems Integration, Independent Design Review). - In regards to the services offered tab we really like the idea that a few people presented that have the outside of our logo with an icon in the middle of consultancy, solutions, etc., etc. Secondly, as mentioned in our brief we really enjoy the design of vortrane site. Specially, we enjoy the strong iconic images they use, the way the tabs at the top scroll easily, and contact us page that generates an email. Lastly, I've included some photos of the concept we have been working on. What we are trying to demonstrate is how our company offers a range of services that are essentially linked together. We provide individual services that when combined present the full service package. We would like this concept to be integrated into the over concept of our website. Please feel free to ask for clarification of any of the above points or contact us if you have any additional questions. We appreciate all of your hard work and are very excited to see the updated designs. Best, Miriam Dowbrook Plenvaro Senior Program Manager miriam.dowbrook@plenvaro-mail.com

Industry/Entity Type

Government

Font styles to use
Serif
Sans Serif

Requirements
Must have
• Must work on/adapt to various/mobile devices (responsive)
Must be simple and straightforward
Colors should be in line/matching with logo
2 language versions: English and Arabic (no Thai)
Services should be the first group/row of items after/below the main image
Note: the website will be hosted by hostpeak
Nice to have
• Submit feedback form
What's New section
The banner at the bottom of the site should not be too large; we would like a narrow one more
It would be nice if the header/top banner (with Home, About, etc. tabs) could stay in place as you scroll down (like Vortrane and Chatterly)
We will likely only use one image with a Company slogan on the Home page rather than a carousel of images to rotate through
Should not have
• This is the existing website: http://www.plenvaro-example.org
We do not like the animation, the way the banner icons/titles bounce
Not simple enough, we don't like the functionality or how pages load so slowly
We do not like the logo centered - it should be at the left
The banner and its tabs should not be towards the right, we would like them to be centered, to go all the way across and to be below the logo

```html
<!DOCTYPE html>
<html lang="en">
<head>
<meta charset="utf-8">
<title>Plenvaro — Systems Knowledge Delivered</title>
<link rel="stylesheet" href="https://fonts.googleapis.com/css2?family=Open+Sans:wght@400;600;700&family=Raleway:wght@400;600;700&display=swap">
<style>
:root{
  --red:#b5161d;
  --red-dark:#8f1016;
  --ink:#333333;
  --muted:#777777;
  --line:#d9d9d9;
  --band:#f1f1f1;
  --white:#ffffff;
  --footer:#a8161c;
  --base:#3a3a3a;
  --button-dark:#2b2b2b;
}
*{box-sizing:border-box;margin:0;padding:0}
html,body{width:1200px;height:2380px;overflow:hidden;background:var(--white)}
body{position:relative;font-family:"Open Sans",Arial,sans-serif;color:var(--ink);font-size:15px}
.abs{position:absolute}
/* top bar */
.topbar{top:0;left:0;width:1200px;height:28px;background:#f7f7f7;border-bottom:1px solid #e6e6e6}
.topbar .contact{right:40px;top:5px;font-size:13px;color:var(--muted);display:flex;gap:14px;align-items:center}
.social{width:20px;height:20px;border-radius:50%;background:#3d8fd1;display:inline-block}
.phone{color:var(--red);font-weight:600}
/* brand */
.brand{left:60px;top:60px;display:flex;align-items:center;gap:16px}
.brand-mark{width:44px;height:44px;background:var(--red)}
.brand-name{font-family:"Raleway",sans-serif;font-weight:700;font-size:38px;letter-spacing:3px;color:var(--red)}
/* nav */
.nav{top:124px;left:370px;display:flex;gap:12px;font-family:"Raleway",sans-serif;font-size:14px;font-weight:600;color:#555;letter-spacing:1px}
.nav a{display:block;padding:7px 22px;text-decoration:none;color:inherit}
.nav a.active{background:var(--red);color:var(--white);border-radius:4px}
.nav-rule{top:164px;left:370px;width:780px;height:2px;background:var(--line)}
/* hero */
.hero{top:192px;left:0;width:1200px;height:536px;background:linear-gradient(100deg,#e6e8ea 0%,#b9bec3 40%,#8c9298 70%,#c7cbcf 100%)}
.hero-tag{top:428px;left:260px;width:680px;height:56px;background:var(--red);color:var(--white);font-family:"Raleway",sans-serif;font-weight:700;font-size:34px;text-align:center;line-height:56px;letter-spacing:1px}
.hero-dots{top:710px;left:560px;display:flex;gap:8px}
.hero-dots span{width:12px;height:12px;border-radius:50%;background:#fff}
.hero-dots span.on{background:var(--red)}
.hero-base{top:728px;left:0;width:1200px;height:8px;background:var(--red)}
/* section titles */
.sec-title{font-family:"Raleway",sans-serif;font-size:28px;color:#555}
.sec-title b{color:var(--red);font-weight:600}
.services-title{top:768px;left:0;width:1200px;text-align:center}
.title-mark{top:816px;left:588px;width:24px;height:24px;border:3px solid var(--red);transform:rotate(45deg)}
.arrows{top:776px;right:60px;display:flex;gap:6px}
/* services */
.service{top:872px;width:340px;display:flex;gap:16px}
.service .icon{flex:none;width:92px;height:92px;display:flex;align-items:center;justify-content:center}
.service h3{font-family:"Raleway",sans-serif;font-size:24px;font-weight:600;color:#444;margin-bottom:6px}
.service p{font-size:14px;line-height:20px;color:var(--muted)}
.btn{display:inline-block;background:var(--red);color:var(--white);font-size:13px;padding:5px 16px;border-radius:3px;margin-top:12px}
.btn.dark{background:#333}
/* who we are */
.who{top:1120px;left:0;width:1200px;height:420px;background:var(--band);border-top:1px solid #e4e4e4}
.who-title{top:1176px;left:72px}
.who-rule{top:1200px;left:250px;width:530px;height:1px;background:var(--line)}
.who-text{top:1246px;left:72px;width:720px;font-size:15px;line-height:24px;color:#555}
.who-btn{top:1420px;left:72px}
.monitor{top:1192px;left:830px;width:330px;height:300px}
.screen{position:absolute;left:0;top:0;width:330px;height:220px;background:#222;border-radius:8px;padding:12px}
.screen div{width:100%;height:100%;background:linear-gradient(135deg,#e9eef3,#9aa8b6)}
.stand{position:absolute;left:135px;top:220px;width:60px;height:50px;background:#c9c9c9}
.foot{position:absolute;left:95px;top:268px;width:140px;height:12px;background:#b7b7b7;border-radius:6px}
/* news & form */
.news-title{top:1590px;left:72px}
.msg-title{top:1590px;left:700px}
.news{left:72px;width:520px;display:flex;gap:24px}
.news .thumb{flex:none;width:160px;height:96px;background:linear-gradient(180deg,#9ec2e6,#8fae6a)}
.news h4{font-size:14px;font-weight:700;color:var(--red);margin-bottom:6px}
.news p{font-size:13px;line-height:19px;color:var(--muted)}
.field{height:36px;border:1px solid #ccc;font-size:13px;color:#888;padding:8px 10px;background:#fff}
.submit{top:1904px;left:700px;width:200px;height:34px;background:var(--red);color:#fff;font-size:13px;font-weight:600;text-align:center;line-height:34px;border-radius:3px}
/* footer */
.footer{top:2040px;left:0;width:1200px;height:300px;background:var(--footer)}
.fcol{top:2092px;color:var(--white)}
.fcol h5{font-size:16px;font-weight:600;margin-bottom:22px;color:var(--white)}
.fcol ul{padding:0}
.fcol li{list-style:none;font-size:13px;margin-bottom:16px;color:var(--white)}
.fcol li::before{content:"›";margin-right:8px}
.newsletter p{font-size:13px;margin-bottom:10px;color:var(--white)}
.newsletter .in{width:190px;height:30px;background:#fff;color:#999;font-size:12px;padding:6px 8px}
.newsletter .go{margin-top:10px;width:110px;height:28px;background:var(--button-dark);color:var(--white);font-size:12px;font-weight:600;text-align:center;line-height:28px}
.flogo{top:2140px;left:960px;display:flex;align-items:center;gap:12px;color:var(--white)}
.flogo .sq{width:36px;height:36px;background:#fff}
.flogo span.name{font-family:"Raleway",sans-serif;font-weight:700;font-size:30px;letter-spacing:3px;color:var(--white)}
.base{top:2340px;left:0;width:1200px;height:40px;background:var(--base);color:#ccc;font-size:12px}
.base .copy{left:72px;top:12px}
.base .links{right:60px;top:12px}
</style>
</head>
<body>
<header>
  <div class="abs topbar">
    <div class="abs contact">
      <span>office@plenvaro-mail.com</span>
      <span class="social"></span><span class="social" style="background:#3b5a9a"></span>
      <span class="phone">02-5550-0147</span>
    </div>
  </div>
  <div class="abs brand"><span class="brand-mark"></span><span class="brand-name">PLENVARO</span></div>
  <nav class="abs nav">
    <a class="active">HOME</a><a>BUSINESS UNIT</a><a>SERVICES</a><a>ABOUT US</a><a>LOCATIONS</a><a>CONTACT US</a>
  </nav>
  <div class="abs nav-rule"></div>
</header>

<section>
  <div class="abs hero" role="img" aria-label="Photo of a hand holding a tablet in front of a server room"></div>
  <div class="abs hero-tag">SYSTEMS KNOWLEDGE DELIVERED</div>
  <div class="abs hero-dots"><span class="on"></span><span></span><span></span><span></span><span></span></div>
  <div class="abs hero-base"></div>
</section>

<section>
  <h2 class="abs sec-title services-title">Services <b>Offered</b></h2>
  <div class="abs title-mark"></div>
  <div class="abs arrows">
    <svg width="14" height="20" viewBox="0 0 14 20"><path d="M11 2L3 10l8 8" stroke="#bbb" stroke-width="3" fill="none"/></svg>
    <svg width="14" height="20" viewBox="0 0 14 20"><path d="M3 2l8 8-8 8" stroke="#b5161d" stroke-width="3" fill="none"/></svg>
  </div>

  <div class="abs service" style="left:60px">
    <div class="icon"><svg width="70" height="70" viewBox="0 0 70 70"><path d="M14 56L44 26" stroke="#333" stroke-width="8" stroke-linecap="round"/><circle cx="48" cy="22" r="10" fill="none" stroke="#b5161d" stroke-width="6"/><path d="M16 16l38 38" stroke="#333" stroke-width="6" stroke-linecap="round"/></svg></div>
    <div><h3>Construction</h3><p>Lorem ipsum dolor sit amet con sect etur adip iscing elit. Ut felis ligula All apiris sim sit amet inter iicm non adip</p><span class="btn">Read more</span></div>
  </div>
  <div class="abs service" style="left:440px">
    <div class="icon"><svg width="70" height="70" viewBox="0 0 70 70"><circle cx="35" cy="35" r="20" fill="none" stroke="#333" stroke-width="10" stroke-dasharray="8 5"/><circle cx="35" cy="35" r="8" fill="#b5161d"/></svg></div>
    <div><h3>Engineering</h3><p>Lorem ipsum dolor sit amet con sect etur adip iscing elit. Ut felis ligula All apiris sim sit amet inter iicm non adip</p><span class="btn dark">Read more</span></div>
  </div>
  <div class="abs service" style="left:800px">
    <div class="icon"><svg width="70" height="70" viewBox="0 0 70 70"><circle cx="35" cy="35" r="30" fill="#333"/><circle cx="26" cy="30" r="7" fill="#fff"/><circle cx="44" cy="30" r="7" fill="#b5161d"/><rect x="16" y="40" width="38" height="12" rx="6" fill="#fff"/></svg></div>
    <div><h3>Consulting</h3><p>Lorem ipsum dolor sit amet con sect etur adip iscing elit. Ut felis ligula All apiris sim sit amet inter iicm non adip</p><span class="btn">Read more</span></div>
  </div>
</section>

<section>
  <div class="abs who"></div>
  <h2 class="abs sec-title who-title">Who <b>we</b> are?</h2>
  <div class="abs who-rule"></div>
  <p class="abs who-text">Plenvaro specializes in delivering quality professional services and technical projects that support larger business goals. Plenvaro are tools that support a greater business function and need. We understand that most technical projects are conceptualized to support a larger vision with actual business goals in mind and ensure that all of our professional and technical expertise is included in our professional services to meet those goals.</p>
  <span class="abs btn who-btn">Read more</span>
  <div class="abs monitor">
    <div class="screen"><div role="img" aria-label="Screen showing a business meeting photo"></div></div>
    <div class="stand"></div><div class="foot"></div>
  </div>
</section>

<section>
  <h2 class="abs sec-title news-title">What's <b>New?</b></h2>
  <div class="abs news" style="top:1672px">
    <div class="thumb" role="img" aria-label="Photo of an engineer in a green field"></div>
    <div><h4>ARTICLE TITLE GOES HERE</h4><p>Lorem ipsum dolor sit amet, consectetur adipiscing elit. Phasellus eget leo leo. Sed adipiscing mi orci, vel ultrices turpis mattis a varius elit dolor ipsum.</p></div>
  </div>
  <div class="abs news" style="top:1832px">
    <div class="thumb" role="img" aria-label="Photo of a worker in a hard hat outdoors"></div>
    <div><h4>ARTICLE TITLE GOES HERE</h4><p>Lorem ipsum dolor sit amet, consectetur adipiscing elit. Phasellus eget leo leo. Sed adipiscing mi orci, vel ultrices turpis mattis a varius elit dolor ipsum.</p></div>
  </div>

  <h2 class="abs sec-title msg-title">Send us a <b>Message</b></h2>
  <div class="abs field" style="top:1666px;left:700px;width:200px">Firstname</div>
  <div class="abs field" style="top:1666px;left:912px;width:200px">Lastname</div>
  <div class="abs field" style="top:1718px;left:700px;width:200px">Phone no.</div>
  <div class="abs field" style="top:1718px;left:912px;width:200px">Email</div>
  <div class="abs field" style="top:1770px;left:700px;width:412px;height:112px">Message..</div>
  <div class="abs submit">SUBMIT</div>
</section>

<footer>
  <div class="abs footer"></div>
  <div class="abs fcol" style="left:140px"><h5>Who we are</h5><ul><li>Sublink here</li><li>Sublink here</li><li>Sublink here</li><li>Sublink here</li><li>Sublink here</li></ul></div>
  <div class="abs fcol" style="left:400px"><h5>What we offer</h5><ul><li>Sublink here</li><li>Sublink here</li><li>Sublink here</li><li>Sublink here</li><li>Sublink here</li></ul></div>
  <div class="abs fcol newsletter" style="left:652px"><h5>Newsletter Signup</h5><p>Subscribe to get updates</p><div class="in">Email address</div><div class="go">SUBMIT</div></div>
  <div class="abs flogo"><span class="sq"></span><span class="name">PLENVARO</span></div>
  <div class="abs base">
    <span class="abs copy">Copyright © 2014 Plenvaro</span>
    <span class="abs links">FAQ &nbsp;|&nbsp; Sitemap &nbsp;|&nbsp; Privacy Policy</span>
  </div>
</footer>
</body>
</html>
```